Quick 1hr job to create exciting page header & footer designs

We need some exciting and engaging header and footer designs for school yearbooks, in particular for the NZ Primary school market (children 5 to 10 years old).
The header and footer designs need to be bright and colourful, and should appeal to younger children. Header and footer graphics do not need to be the same, but should at least relate to each other thematically.
Please include the following sample text on the header: Sports Day.
Please include this sample text on the footer: Primary School Name 2014.
Note that the header/footers may be used without the text so the design should work with or without the text. Header/footer may be used over top of a coloured or graphic background. The graphic could be illustrative, photographic or patterned, the more creative the better.

Header dimensions: 198.88 mm w x 15.24 mm h
Footer dimensions: 198.88 mm w x 6.35 mm h

Please see the example pages provided, but please note we are looking for something more suitable for Primary Schools, and a lot more dynamic and interesting!

Target Market(s)

New Zealand Primary Schools

Industry/Entity Type

School

Requirements
Must have
• Must contain sample text and must be suitable for younger children
• Must be appropriate for the New Zealand market, i.e. don't use imagery that is obviously from other countries.

```html
<!DOCTYPE html>
<html lang="en">
<head>
<meta charset="UTF-8">
<title>Sports Day – Header &amp; Footer</title>
<link rel="stylesheet" href="https://fonts.googleapis.com/css2?family=Caveat+Brush&family=Jost:wght@300&display=swap">
<style>
  :root {
    --page: #ffffff;
    --field-green: #21903f;
    --field-green-edge: #3aa457;
    --title-red: #ef1a2a;
    --title-glow: #33e03a;
    --footer-red: #e8141f;
    --shoe-navy: #1b2f8f;
    --shoe-sky: #41b4e0;
  }

  * { margin: 0; padding: 0; box-sizing: border-box; }

  html, body {
    width: 1200px;
    height: 300px;
    overflow: hidden;
    background: var(--page);
  }

  .canvas {
    position: relative;
    width: 1200px;
    height: 300px;
    background: var(--page);
  }

  .band {
    position: absolute;
    left: 71px;
    width: 1062px;
    background: var(--field-green);
    box-shadow: 0 0 3px 1px var(--field-green-edge);
  }

  .band--header { top: 70px; height: 78px; }
  .band--footer { top: 198px; height: 34px; }

  .shoe {
    position: absolute;
    display: block;
  }

  .band--header .shoe { top: 7px; width: 95px; height: 74px; }
  .band--header .shoe--left { left: 15px; }
  .band--header .shoe--right { right: 19px; }

  .band--footer .shoe { top: -3px; width: 82px; height: 37px; }
  .band--footer .shoe--left { left: 20px; }
  .band--footer .shoe--right { right: 23px; }

  .band__title {
    position: absolute;
    left: 0;
    right: 0;
    top: -4px;
    text-align: center;
    font-family: "Caveat Brush", cursive;
    font-size: 76px;
    line-height: 1;
    letter-spacing: 1px;
    color: var(--title-red);
    text-shadow: 3px 2px 0 var(--title-glow);
  }

  .band__caption {
    position: absolute;
    left: 0;
    right: 0;
    top: 0;
    text-align: center;
    font-family: "Jost", sans-serif;
    font-weight: 300;
    font-size: 31px;
    line-height: 34px;
    color: var(--footer-red);
  }
</style>
</head>
<body>
  <main class="canvas">
    <header class="band band--header">
      <svg class="shoe shoe--left" viewBox="0 0 95 74" role="img" aria-label="Illustration of a blue running shoe">
        <defs>
          <linearGradient id="shoe-tone-a" x1="0" y1="0" x2="1" y2="1">
            <stop offset="0" stop-color="var(--shoe-sky)"/>
            <stop offset="1" stop-color="var(--shoe-navy)"/>
          </linearGradient>
        </defs>
        <rect width="95" height="74" rx="10" fill="url(#shoe-tone-a)"/>
      </svg>
      <h1 class="band__title">SPORTS DAY</h1>
      <svg class="shoe shoe--right" viewBox="0 0 95 74" role="img" aria-label="Illustration of a blue running shoe">
        <rect width="95" height="74" rx="10" fill="url(#shoe-tone-a)"/>
      </svg>
    </header>

    <footer class="band band--footer">
      <svg class="shoe shoe--left" viewBox="0 0 82 37" role="img" aria-label="Illustration of a blue running shoe, cropped">
        <defs>
          <linearGradient id="shoe-tone-b" x1="0" y1="0" x2="1" y2="1">
            <stop offset="0" stop-color="var(--shoe-sky)"/>
            <stop offset="1" stop-color="var(--shoe-navy)"/>
          </linearGradient>
        </defs>
        <rect width="82" height="37" rx="8" fill="url(#shoe-tone-b)"/>
      </svg>
      <p class="band__caption">PRIMARY SCHOOL 2014</p>
      <svg class="shoe shoe--right" viewBox="0 0 82 37" role="img" aria-label="Illustration of a blue running shoe, cropped">
        <rect width="82" height="37" rx="8" fill="url(#shoe-tone-b)"/>
      </svg>
    </footer>
  </main>
</body>
</html>
```